business cards for heating company

I need business cards for my heating air conditioning and chimney company located in upstate NY I would like for them to be colorful and catchy on heavy stock with preferably a glossy finish on front of card but the ability to write something on one half of the back with maybe some bullets on the other half of the back I also need to be able to change the name and title of employees on the card and also incorporate some of our current look and feel from our trucks and website I also want to be able to use this design or similar to have door hangers made lawn signs coffee mugs key chains etc. our website is Brindlecove.com

Target Market(s)

homeowners

Industry/Entity Type

Air Conditioning

Contact Information for Business Card

should have website brindlecove.com , phone number 585-437-9184 please look at website for ideas

Font styles to use
Sans Serif

Colors
ec1f27
3176b5
fbee3f

Requirements
Must have
• a complete look
Nice to have
• a discount offer like 10% military and first responders
• senior discount %5

```html
<!DOCTYPE html>
<html lang="en">
<head>
<meta charset="utf-8">
<title>Brindle Cove — Business Cards</title>
<link href="https://fonts.googleapis.com/css2?family=Jost:wght@400;500;700&display=swap" rel="stylesheet">
<style>
  :root {
    --bg: #e9e6e1;
    --card-back: #c4435f;
    --card-white: #ffffff;
    --brand-blue: #2a5fa8;
    --brand-red: #d7342d;
    --brand-yellow: #dcc33d;
    --ink-light: #ffffff;
    --ink-muted: rgba(255,255,255,0.85);
  }
  * { margin: 0; padding: 0; box-sizing: border-box; }
  html, body { width: 1200px; height: 904px; overflow: hidden; }
  body {
    background: var(--bg);
    font-family: "Jost", sans-serif;
    position: relative;
  }
  .card {
    position: absolute;
    width: 680px;
    height: 388px;
    border-radius: 4px;
    box-shadow: 0 10px 24px rgba(0,0,0,0.22);
    overflow: hidden;
  }
  /* Back side */
  .card--back {
    left: 90px; top: 50px;
    background: var(--card-back);
    color: var(--ink-light);
    text-align: center;
  }
  .card--back .brand-name {
    position: absolute; left: 0; right: 0; top: 128px;
  }
  .card--back .offers {
    position: absolute; left: 0; right: 0; top: 250px;
    font-size: 15px; line-height: 1.45; color: var(--ink-muted);
  }
  .brand-name {
    display: flex; align-items: center; justify-content: center; gap: 12px;
    font-weight: 700; font-size: 38px; letter-spacing: 1px; text-transform: uppercase;
  }
  .brand-mark { width: 22px; height: 22px; background: currentColor; }

  /* Front side */
  .card--front {
    left: 430px; top: 466px;
    background: var(--card-white);
  }
  .card--front .wave { position: absolute; inset: 0; }
  .card--front .brand-name {
    position: absolute; left: 44px; top: 112px;
    justify-content: flex-start;
    color: var(--brand-red);
    font-size: 36px;
  }
  .contact {
    position: absolute; right: 46px; top: 164px;
    color: var(--ink-light); text-align: right;
  }
  .contact .person-name { font-size: 22px; font-weight: 500; line-height: 1.2; }
  .contact .person-title { font-size: 14px; margin-top: 2px; margin-bottom: 22px; }
  .contact .address { font-size: 16px; line-height: 1.35; }
  .contact-line {
    display: flex; justify-content: flex-end; align-items: center; gap: 10px;
    font-size: 16px; line-height: 1.45;
  }
  .contact-line svg { width: 15px; height: 15px; fill: var(--ink-light); }
</style>
</head>
<body>

<section class="card card--back" aria-label="Business card back">
  <div class="brand-name"><span class="brand-mark"></span>Brindle Cove</div>
  <div class="offers">
    <p>- a discount offer like 10% military and first responders</p>
    <p>- senior discount %5</p>
  </div>
</section>

<section class="card card--front" aria-label="Business card front">
  <svg class="wave" viewBox="0 0 680 388" preserveAspectRatio="none" aria-hidden="true">
    <path d="M0,300 C220,292 320,270 400,160 C460,80 560,40 680,28 L680,40 C565,52 470,92 412,172 C332,282 228,304 0,312 Z" fill="var(--brand-yellow)"/>
    <path d="M0,322 C230,312 330,290 410,178 C470,96 565,62 680,50 L680,72 C572,84 482,116 424,196 C344,306 240,330 0,342 Z" fill="var(--brand-red)"/>
    <path d="M0,350 C245,340 350,318 430,206 C490,124 580,92 680,80 L680,388 L0,388 Z" fill="var(--brand-blue)"/>
  </svg>

  <div class="brand-name"><span class="brand-mark"></span>Brindle Cove</div>

  <div class="contact">
    <p class="person-name">Dana Whitfield</p>
    <p class="person-title">Manager</p>
    <p class="address">318 Alder Lane</p>
    <p class="address">Fairport, NY 14450</p>
    <p class="contact-line">585-437-9184
      <svg viewBox="0 0 24 24"><path d="M6.6 10.8a15.1 15.1 0 0 0 6.6 6.6l2.2-2.2c.3-.3.7-.4 1-.2 1.1.4 2.3.6 3.6.6.6 0 1 .4 1 1V20c0 .6-.4 1-1 1A17 17 0 0 1 3 4c0-.6.4-1 1-1h3.5c.6 0 1 .4 1 1 0 1.3.2 2.5.6 3.6.1.3 0 .7-.2 1z"/></svg>
    </p>
    <p class="contact-line">info@brindlecove.com
      <svg viewBox="0 0 24 24"><path d="M2 5h20v14H2z M3 6l9 7 9-7" fill="none" stroke="#fff" stroke-width="2"/></svg>
    </p>
    <p class="contact-line">brindlecove.com
      <svg viewBox="0 0 24 24"><circle cx="12" cy="12" r="9" fill="none" stroke="#fff" stroke-width="2"/><path d="M3 12h18M12 3c3 3 3 15 0 18M12 3c-3 3-3 15 0 18" fill="none" stroke="#fff" stroke-width="1.6"/></svg>
    </p>
  </div>
</section>

</body>
</html>
```